Typographic word art illustration of life lessons

I've written out all the meaningful life lessons my parents have taught me and would like to give it to them for Christmas in the form of a typographic word art design. This will be a print project. I'd like the size of the design to be no larger than 11x17, no smaller than 8.5x11.
The text must be readable in the complete sentences provided.
The text can be displayed in multiple directions, as long as each sentence is readable.
The text itself should be arranged in an artistic and creative way. I'm not looking for text that is aligned in normal-looking rows with a an image watermark behind it.
Sentences may be included on the same row if it works with the design.
Font, Case and Text may be alternated to best suite your design. No grunge fonts, or small-size handwriting fonts, or anything that is difficult to read.
Text could fit into a shape or silhouette (ie: heart, tree, or anything that symbolizes family, life, love, etc.), or form an abstract design, or it can be justified to fit the whole page.
I'm not looking for anything super colorful. Black and white would work, or any standard color palette. The intended result is something they can hang on their wall.
Text is attached in a pdf. Minor tweaks to text is ok if necessary for formatting design, but in general, text should remain unedited.
I've also added some examples of the type of word art I had in mind.
Please help me make this gift into something beautiful and special!
Updates
I trimmed the text down significantly because all the designs seemed to crowded, and had to use fonts that were too small. Here is the revised text:
Don’t give up until you’ve given your all.
Don’t let people that hurt you occupy your mind.
Good people do bad things. Get over it.
Block bitterness from ever taking root in your heart.
Take every opportunity to express gratitude.
True brotherhood is forged out of loyalty and love.
There is no excuse for deceit.
Words matter.
Forgiveness is not optional.
Never make insincere apologies.
Worrying is a waste of time.
Choose your destiny by choosing your friends.
Marriage is a unified front. Make your spouse a priority.
Truth and grace are inseparable.
Humor disarms, softens and endears.
Selflessness is a lifestyle.
Whenever possible, give generously and anonymously.
Never apologize and give an excuse in the same sentence.
Faith must fuel the core of who you are.
The path to freedom begins with asking difficult questions.
Take advantage of every opportunity to educate yourself.
Be your spouse’s protector and advocate.
Radiate humility, vulnerability and love.
Give your finish line the ability to expand.

```html
<!DOCTYPE html>
<html lang="en">
<head>
<meta charset="utf-8">
<title>Words Matter</title>
<link href="https://fonts.googleapis.com/css2?family=Raleway:wght@200;300;400;500&family=Montserrat:wght@600;700;800&display=swap" rel="stylesheet">
<style>
  :root {
    --ground: #3c3c3c;
    --ink: #f4f4f4;
    --rule: #a0a0a0;
    --thin: "Raleway", sans-serif;
    --bold: "Montserrat", sans-serif;
  }
  html, body { margin: 0; padding: 0; overflow: hidden; background: var(--ground); }
  .poster {
    position: relative; width: 776px; height: 1200px; overflow: hidden;
    background: var(--ground); color: var(--ink);
    font-family: var(--thin); font-weight: 300; text-transform: uppercase;
  }
  .block { position: absolute; margin: 0; }
  .line {
    display: block; white-space: nowrap;
    text-align: justify; text-align-last: justify;
  }
  .b { font-family: var(--bold); font-weight: 700; }
  .m { font-weight: 500; }
  .rule { position: absolute; height: 1px; background: var(--rule); }
  .vrule { position: absolute; width: 1px; background: var(--rule); }
  .frame { position: absolute; border: 1.5px solid var(--ink); box-sizing: border-box; }
  .title { position: absolute; left: 0; top: 0; }

  .bitterness { left: 47px; top: 232px; width: 232px; font-size: 20.5px; line-height: 26px; letter-spacing: 1px; }
  .gratitude { left: 298px; top: 236px; width: 432px; font-size: 15px; line-height: 20px; }
  .forgiveness { left: 298px; top: 268px; width: 432px; font-size: 24px; line-height: 34px; }

  .judge { left: 47px; top: 321px; width: 102px; font-size: 19px; line-height: 25.8px; letter-spacing: 1px; }
  .judge .b { font-size: 16.5px; letter-spacing: 0; }
  .give-all { left: 166px; top: 321px; width: 404px; font-size: 29px; line-height: 36px; letter-spacing: 4px; }
  .give-all .b { font-size: 26px; letter-spacing: .5px; }
  .good-people { left: 164px; top: 403px; width: 150px; height: 72px; padding: 6px 7px; font-size: 15px; line-height: 20px; letter-spacing: .3px; }
  .insincere { left: 166px; top: 484px; width: 140px; font-size: 19px; line-height: 22px; letter-spacing: 1px; }
  .insincere .b { font-size: 18px; letter-spacing: 1.5px; }
  .in-need { left: 338px; top: 400px; width: 232px; font-size: 18px; line-height: 26px; letter-spacing: 3px; }
  .generously { left: 338px; top: 490px; width: 230px; height: 26px; padding: 0 6px; font-size: 21px; line-height: 24px; font-weight: 300; }
  .anonymously { left: 338px; top: 518px; width: 230px; height: 26px; padding: 0 6px; box-sizing: border-box; background: var(--ink); color: var(--ground); font-size: 18px; line-height: 26px; letter-spacing: 1.5px; }
  .choose { left: 590px; top: 330px; width: 142px; height: 116px; padding: 4px 7px; font-size: 16.5px; line-height: 25px; letter-spacing: 1px; }
  .choose .lead { font-size: 26px; line-height: 36px; text-align: center; text-align-last: center; letter-spacing: 0; }
  .marriage { left: 590px; top: 452px; width: 142px; font-size: 15.5px; line-height: 20px; letter-spacing: 1px; }
  .marriage .b { font-size: 14.5px; letter-spacing: 0; }
  .marriage .wide { font-size: 18px; letter-spacing: 3px; }
  .marriage .lead { font-size: 25px; line-height: 32px; letter-spacing: 0; }

  .truth { left: 54px; top: 566px; width: 130px; font-size: 17px; line-height: 24px; letter-spacing: .3px; }
  .freedom { left: 201px; top: 566px; width: 244px; font-size: 17.5px; line-height: 24px; letter-spacing: 1.5px; }
  .potential { left: 458px; top: 567px; width: 274px; height: 70px; padding: 2px 6px; font-size: 16px; line-height: 22px; letter-spacing: 1.5px; }
  .potential .spread { letter-spacing: 3px; }
  .potential .b { letter-spacing: 2px; }

  .humor { left: 47px; top: 654px; width: 398px; font-size: 18px; line-height: 24px; }
  .finish { left: 47px; top: 683px; width: 398px; font-size: 30px; line-height: 36px; letter-spacing: 2px; }
  .finish .small { font-size: 21px; }
  .spouse { left: 47px; top: 768px; width: 400px; font-size: 15.5px; line-height: 22px; }
  .faith { left: 466px; top: 651px; width: 264px; font-size: 21px; line-height: 23px; letter-spacing: 1px; }
  .educate { left: 466px; top: 707px; width: 264px; font-size: 20px; line-height: 28px; }
  .educate .lead { font-size: 23px; }

  .apologize { left: 47px; top: 803px; width: 344px; font-size: 29.5px; line-height: 37px; letter-spacing: 1.5px; }
  .stand-up { left: 404px; top: 809px; width: 330px; height: 26px; padding: 0 6px; font-size: 18px; line-height: 24px; letter-spacing: 1px; }
  .themselves { left: 404px; top: 838px; width: 330px; height: 26px; padding: 0 6px; box-sizing: border-box; background: var(--ink); color: var(--ground); font-size: 17.5px; line-height: 26px; letter-spacing: 1px; }
  .hurt { left: 404px; top: 866px; width: 330px; font-size: 19px; line-height: 26px; letter-spacing: 1px; }
  .hurt .b { font-size: 20px; }

  .children { left: 50px; top: 930px; width: 384px; font-size: 19px; line-height: 25px; letter-spacing: 1px; }
  .children .b { font-size: 24px; line-height: 28px; letter-spacing: 0; }
  .selflessness { left: 458px; top: 930px; width: 272px; font-size: 32px; line-height: 36px; }
  .selflessness .sub { font-size: 17px; line-height: 22px; letter-spacing: 3px; }
  .worrying { left: 47px; top: 995px; width: 389px; height: 44px; padding: 0 8px; display: flex; align-items: center; gap: 12px; }
  .worrying .word { font-size: 37px; letter-spacing: 2px; line-height: 1; }
  .worrying .aside { font-size: 15.5px; line-height: 15px; letter-spacing: 1px; }
  .family { left: 462px; top: 998px; width: 268px; font-size: 16px; line-height: 22px; }

  .willpower { left: 47px; top: 1070px; width: 683px; font-size: 34px; line-height: 42px; letter-spacing: 2px; }
  .willpower .b { font-size: 36px; letter-spacing: 12px; }
</style>
</head>
<body>
<main class="poster">
  <svg class="title" width="776" height="190" viewBox="0 0 776 190" aria-labelledby="title-text">
    <defs><path id="title-arc" d="M 190 150 Q 395 10 605 162"/></defs>
    <text id="title-text" fill="var(--ink)" font-family="Raleway, sans-serif" font-weight="200" font-size="40" letter-spacing="4">
      <textPath href="#title-arc" startOffset="50%" text-anchor="middle">WORDS MATTER</textPath>
    </text>
    <g class="heart" fill="none" stroke="var(--ink)" stroke-width="2">
      <path d="M395 162 C370 145 375 120 388 122 C393 123 395 128 395 130 C395 128 397 123 402 122 C415 120 420 145 395 162 Z"/>
      <path d="M395 155 C377 142 381 126 390 127 C393 128 395 131 395 134 C395 131 397 128 400 127 C409 126 413 142 395 155 Z"/>
    </g>
  </svg>

  <div class="rule" style="left:44px;top:227px;width:686px"></div>
  <p class="block bitterness">
    <span class="line">Block bitterness</span>
    <span class="line">from ever taking</span>
    <span class="line">root in your <span class="b">heart</span></span>
  </p>
  <p class="block gratitude b"><span class="line">Take every opportunity to express gratitude.</span></p>
  <div class="rule" style="left:292px;top:259px;width:438px"></div>
  <p class="block forgiveness b"><span class="line">Forgiveness is not optional.</span></p>
  <div class="rule" style="left:44px;top:311px;width:686px"></div>

  <p class="block judge">
    <span class="line">Y o u</span>
    <span class="line">D o n ’ t</span>
    <span class="line">have the</span>
    <span class="line">right to</span>
    <span class="line">j u d g e ,</span>
    <span class="line b">but you</span>
    <span class="line b">have the</span>
    <span class="line b">c h o i c e</span>
    <span class="line b">to help.</span>
  </p>
  <p class="block give-all">
    <span class="line">Don’t give up until</span>
    <span class="line b">You’ve given your all.</span>
  </p>
  <p class="block frame good-people">
    <span class="line">Good people</span>
    <span class="line">do bad things.</span>
    <span>Get over it.</span>
  </p>
  <p class="block insincere">
    <span class="line">Never make</span>
    <span class="b">Insincere</span>
    <span class="line">Apologies.</span>
  </p>
  <div class="vrule" style="left:328px;top:402px;height:142px"></div>
  <p class="block in-need m">
    <span class="line">People in need</span>
    <span class="line">shouldn’t need to</span>
    <span class="line">ask for your help.</span>
  </p>
  <p class="block frame generously"><span class="line">Give generously</span></p>
  <p class="block anonymously b"><span class="line">&amp; anonymously.</span></p>
  <div class="block frame choose">
    <span class="line b lead">Choose</span>
    <span class="line">your destiny</span>
    <span class="line">by choosing</span>
    <span class="line">your friends.</span>
  </div>
  <p class="block marriage">
    <span class="line">Marriage is a</span>
    <span class="line b">unified front.</span>
    <span class="line wide">Make your</span>
    <span class="line wide">spouse a</span>
    <span class="line b lead">Priority!</span>
  </p>
  <div class="rule" style="left:44px;top:557px;width:686px"></div>

  <p class="block truth">
    <span class="line">Truth and</span>
    <span class="line">grace are</span>
    <span class="line">inseparable.</span>
  </p>
  <p class="block freedom m">
    <span class="line">The path to freedom</span>
    <span class="line">begins with asking</span>
    <span class="line">difficult questions.</span>
  </p>
  <p class="block frame potential">
    <span class="line">The only standard worth</span>
    <span class="line spread">striving for is your</span>
    <span class="line b">own full potential.</span>
  </p>
  <div class="rule" style="left:44px;top:648px;width:686px"></div>

  <p class="block humor b"><span class="line">Humor disarms, softens &amp; endears.</span></p>
  <div class="rule" style="left:44px;top:681px;width:402px"></div>
  <p class="block finish">
    <span class="line">Give your finish line</span>
    <span class="line"><span class="small">the</span> ability to expand</span>
  </p>
  <div class="rule" style="left:44px;top:761px;width:402px"></div>
  <p class="block spouse b"><span class="line">Be your spouse’s protector &amp; advocate.</span></p>
  <p class="block faith">
    <span class="line">Faith must fuel the</span>
    <span class="line"><span class="b">core</span> of who you are.</span>
  </p>
  <div class="rule" style="left:460px;top:700px;width:270px"></div>
  <p class="block educate b">
    <span class="line">Take advantage of</span>
    <span class="line">every opportunity to</span>
    <span class="line lead">educate yourself.</span>
  </p>
  <div class="rule" style="left:44px;top:798px;width:686px"></div>

  <p class="block apologize">
    <span class="line">Never apologize &amp;</span>
    <span class="line">give an <span class="b">excuse</span> in</span>
    <span class="line">the same sentence.</span>
  </p>
  <p class="block frame stand-up"><span class="line">Stand up for those who can’t</span></p>
  <p class="block themselves b"><span class="line">Stand up for themselves.</span></p>
  <p class="block hurt">
    <span class="line">Don’t let people that hurt</span>
    <span class="line b">You occupy your mind.</span>
  </p>
  <div class="rule" style="left:44px;top:924px;width:686px"></div>

  <p class="block children">
    <span class="line">Show your children humility,</span>
    <span class="line b">Vulnerability and love.</span>
  </p>
  <div class="vrule" style="left:446px;top:932px;height:50px"></div>
  <p class="block selflessness">
    <span class="line b">Selflessness</span>
    <span class="line sub">I s &#160; a &#160; l i f e s t y l e .</span>
  </p>
  <div class="block frame worrying">
    <span class="word">Worrying</span>
    <span class="aside">is a waste<br>of time</span>
  </div>
  <p class="block family">
    <span class="line b">Friends may come and go,</span>
    <span class="line">but family <span class="b">never</span> changes.</span>
  </p>
  <div class="rule" style="left:44px;top:1058px;width:686px"></div>

  <p class="block willpower">
    <span class="line">Willpower can empower you to</span>
    <span class="line b">Accomplish anything</span>
  </p>
</main>
</body>
</html>
```